Business card design needed for Automotive Reconditioning business

I have a logo design i just cant decide on the best color or layout for the business card, I will upload all the files so you can see all colors schemes we are considering. I have other file formats if needed let me know.

Target Market(s)

automotive dealerships

Contact Information for Business Card

HERE are the Descriptions and info needed on the card:
Interior Repair: Leather carpet burns panels dash Deoderize
Dealer products and Vin Verify
( spot for name and cell number) My name is Norman Bexley phone 614 352-4180 Title COO www.QuorvalMotive.com

Font styles to use
Sans Serif
Other font styles liked:
• what ever you think looks best

Requirements
Must have
• Must be able to change the name and phone for employees

```html
<!DOCTYPE html>
<html lang="en">
<head>
<meta charset="utf-8">
<title>Quorval Motive Reconditioning Corp. – Business Card</title>
<link rel="stylesheet" href="https://fonts.googleapis.com/css2?family=Montserrat:wght@700&family=Open+Sans:wght@300;400;600&display=swap">
<style>
  :root {
    --page: #e4e0d9;
    --card-black: #141414;
    --card-black-soft: #2b2b2b;
    --gloss: rgba(255,255,255,0.10);
    --green: #8cc63f;
    --green-light: #a5d65a;
    --green-deep: #6fa82a;
    --white: #ffffff;
    --grey-text: #c9c9c9;
    --grey-muted: #9a9a9a;
  }
  * { box-sizing: border-box; margin: 0; padding: 0; }
  html, body {
    width: 771px; height: 1200px; overflow: hidden;
    background: var(--page);
  }
  .canvas {
    position: relative; width: 771px; height: 1200px;
    display: flex; flex-direction: column; align-items: center; justify-content: center;
    gap: 110px;
  }
  .card {
    position: relative; width: 640px; height: 366px;
    border-radius: 22px; overflow: hidden;
    background:
      linear-gradient(110deg, transparent 30%, var(--gloss) 42%, transparent 56%),
      linear-gradient(160deg, var(--card-black-soft) 0%, var(--card-black) 60%, #0c0c0c 100%);
    box-shadow: 0 14px 30px rgba(0,0,0,0.25);
  }

  /* ---------- shared brand name ---------- */
  .brand {
    position: absolute; display: flex; align-items: center; gap: 12px;
    font-family: "Montserrat", sans-serif; font-weight: 700;
    color: var(--white); text-transform: uppercase; line-height: 1.1;
  }
  .brand-square { flex: none; background: var(--green); }

  /* ---------- back: contact side ---------- */
  .card-back .band { position: absolute; inset: 0; width: 100%; height: 100%; }
  .card-back .brand { top: 52px; right: 44px; font-size: 19px; width: 290px; }
  .card-back .brand-square { width: 16px; height: 16px; }

  .person { position: absolute; left: 44px; top: 70px; }
  .person-name {
    font-family: "Open Sans", sans-serif; font-size: 22px; letter-spacing: 1px;
    color: var(--white); text-transform: uppercase;
  }
  .person-name .given { font-weight: 600; }
  .person-name .family { font-weight: 300; color: var(--grey-text); }
  .person-title {
    margin-top: 6px; font-family: "Open Sans", sans-serif; font-weight: 400;
    font-size: 14px; letter-spacing: 2px; color: var(--green);
  }
  .person-rule { margin-top: 14px; width: 40px; height: 2px; background: var(--green); }

  .contacts {
    position: absolute; left: 0; right: 0; bottom: 42px;
    display: flex; justify-content: space-around; padding: 0 20px;
  }
  .contact { display: flex; flex-direction: column; align-items: center; gap: 10px; }
  .contact svg { width: 18px; height: 18px; }
  .contact-text {
    font-family: "Open Sans", sans-serif; font-weight: 400; font-size: 14px;
    color: var(--white); letter-spacing: 0.3px;
  }

  /* ---------- front: brand side ---------- */
  .card-front .brand {
    left: 50%; top: 112px; transform: translateX(-50%);
    font-size: 30px; width: 470px; justify-content: center; text-align: center;
  }
  .card-front .brand-square { width: 24px; height: 24px; }
  .card-front .rule {
    position: absolute; left: 50%; top: 234px; transform: translateX(-50%);
    width: 40px; height: 2px; background: var(--green);
  }
  .card-front .website {
    position: absolute; left: 0; right: 0; top: 262px; text-align: center;
    font-family: "Open Sans", sans-serif; font-weight: 400; font-size: 14px;
    letter-spacing: 4px; color: var(--grey-text); text-transform: uppercase;
  }
</style>
</head>
<body>
<main class="canvas">

  <!-- contact side -->
  <section class="card card-back" aria-label="Business card, contact side">
    <svg class="band" viewBox="0 0 640 366" preserveAspectRatio="none" aria-hidden="true">
      <defs>
        <linearGradient id="bandFill" x1="0" y1="0" x2="1" y2="1">
          <stop offset="0" stop-color="#a5d65a"/>
          <stop offset="1" stop-color="#7dba34"/>
        </linearGradient>
      </defs>
      <polygon points="0,196 170,196 200,166 640,166 640,366 0,366" fill="url(#bandFill)"/>
      <polygon points="0,196 170,196 200,166 640,166 640,172 203,172 173,202 0,202" fill="#6fa82a" opacity="0.6"/>
    </svg>

    <div class="person">
      <p class="person-name"><span class="given">Norman</span> <span class="family">Bexley</span></p>
      <p class="person-title">COO</p>
      <div class="person-rule"></div>
    </div>

    <div class="brand">
      <span class="brand-square"></span>
      <span>Quorval Motive Reconditioning Corp.</span>
    </div>

    <div class="contacts">
      <div class="contact">
        <svg viewBox="0 0 24 24" aria-hidden="true"><path fill="#1a1a1a" d="M6.6 10.8a15.1 15.1 0 0 0 6.6 6.6l2.2-2.2a1 1 0 0 1 1-.25 11.4 11.4 0 0 0 3.6.57 1 1 0 0 1 1 1V20a1 1 0 0 1-1 1A17 17 0 0 1 3 4a1 1 0 0 1 1-1h3.5a1 1 0 0 1 1 1c0 1.25.2 2.45.57 3.57a1 1 0 0 1-.25 1z"/></svg>
        <span class="contact-text">614 352-4180</span>
      </div>
      <div class="contact">
        <svg viewBox="0 0 24 24" aria-hidden="true"><rect x="3" y="5" width="18" height="14" rx="1.5" fill="none" stroke="#1a1a1a" stroke-width="2"/><path d="M3.5 6l8.5 7 8.5-7" fill="none" stroke="#1a1a1a" stroke-width="2"/></svg>
        <span class="contact-text">hello@quorvalmotive.com</span>
      </div>
      <div class="contact">
        <svg viewBox="0 0 24 24" aria-hidden="true"><circle cx="12" cy="12" r="9" fill="none" stroke="#1a1a1a" stroke-width="2"/><ellipse cx="12" cy="12" rx="4" ry="9" fill="none" stroke="#1a1a1a" stroke-width="1.6"/><path d="M3 12h18M5 7h14M5 17h14" stroke="#1a1a1a" stroke-width="1.6"/></svg>
        <span class="contact-text">www.QuorvalMotive.com</span>
      </div>
    </div>
  </section>

  <!-- brand side -->
  <section class="card card-front" aria-label="Business card, brand side">
    <div class="brand">
      <span class="brand-square"></span>
      <span>Quorval Motive Reconditioning Corp.</span>
    </div>
    <div class="rule"></div>
    <p class="website">www.QuorvalMotive.com</p>
  </section>

</main>
</body>
</html>
```